Business card design needed

We are 2 artists starting up a studio by the water in Sydney ...where we can work and display our art...would like the back ground to be Navy and white stripe...nautical...and the name The Paint Hut to be bold and the main wording...not nautical...if possible thought the A for art could be an easel ...ie the capital A using the cross bar as the platform that paint would be circles of colour....would like the main wording in Black but the easel A in colour
Hope u are able to help
thanku Lorna Vesk
as I will be away in a week for 4 weeks could u please send all info to Mira Colbins email....she can contact me and we can go ahead asap....

Artists

THE PAINT HUT

Hallorans Oar House
The Reach..17 Kellaby Rd..Dunrook 2091 Sydney

Mir Colbin..0437819025..miracolbin@mailnest.example
Lorn Vesk...0429573816..lvesk@harborlink.example

```html
<!DOCTYPE html>
<html lang="en">
<head>
<meta charset="utf-8">
<title>The Paint Hut – Business Card</title>
<link rel="stylesheet" href="https://fonts.googleapis.com/css2?family=Source+Sans+3:wght@400;600&display=swap">
<style>
  :root {
    --navy: #22409a;
    --stripe-white: #ffffff;
    --text-white: #ffffff;
    --backdrop: #ece7df;
    --stripe-period: 23.3px;
    --stripe-line: 5px;
  }
  html, body {
    margin: 0;
    padding: 0;
    width: 1200px;
    height: 772px;
    overflow: hidden;
    background: var(--backdrop);
  }
  .card {
    position: absolute;
    left: 50px;
    top: 68px;
    width: 1100px;
    height: 636px;
    background: var(--navy);
    font-family: "Source Sans 3", "Myriad Pro", Arial, sans-serif;
    color: var(--text-white);
    overflow: hidden;
  }
  .stripes {
    position: absolute;
    top: 0;
    bottom: 0;
    background: repeating-linear-gradient(
      to bottom,
      var(--navy) 0,
      var(--navy) calc(var(--stripe-period) - var(--stripe-line)),
      var(--stripe-white) calc(var(--stripe-period) - var(--stripe-line)),
      var(--stripe-white) var(--stripe-period)
    );
  }
  .stripes--left { left: 0; width: 305px; }
  .stripes--right { right: 0; width: 122px; }

  .content {
    position: absolute;
    left: 305px;
    right: 122px;
    top: 0;
    bottom: 0;
    text-align: center;
  }
  .brand {
    position: absolute;
    left: 0;
    right: 0;
    top: 96px;
    display: flex;
    justify-content: center;
    align-items: center;
    gap: 16px;
  }
  .brand__dot {
    width: 34px;
    height: 34px;
    border-radius: 50%;
    background: var(--text-white);
  }
  .brand__name {
    font-size: 64px;
    font-weight: 600;
    line-height: 1;
    letter-spacing: -0.5px;
  }
  .contact {
    position: absolute;
    left: 0;
    right: 0;
    margin: 0;
    line-height: 1.15;
  }
  .contact__name { font-size: 34px; font-weight: 400; }
  .contact__phone { font-size: 27px; }
  .contact__email { display: block; font-size: 26px; margin-top: 4px; }
  .contact--first { top: 280px; }
  .contact--second { top: 393px; }
  .address {
    position: absolute;
    left: 0;
    right: 0;
    top: 510px;
    margin: 0;
    font-size: 25px;
    line-height: 1.45;
    font-style: normal;
  }
</style>
</head>
<body>
  <div class="card">
    <div class="stripes stripes--left"></div>
    <div class="stripes stripes--right"></div>

    <div class="content">
      <div class="brand">
        <span class="brand__dot"></span>
        <span class="brand__name">The Paint Hut</span>
      </div>

      <p class="contact contact--first">
        <span class="contact__name">COLBIN</span>
        <span class="contact__phone"> : 0437819025</span>
        <span class="contact__email">miracolbin@mailnest.example</span>
      </p>

      <p class="contact contact--second">
        <span class="contact__name">LORN VESK</span>
        <span class="contact__phone"> : 0429573816</span>
        <span class="contact__email">lvesk@harborlink.example</span>
      </p>

      <address class="address">
        Hallorans Oar House, The Reach..17 Kellaby Rd.<br>
        Dunrook 2091, Sydney Lorn
      </address>
    </div>
  </div>
</body>
</html>
```